KTR Business Card

We need a new design for our business cards. We are brokers in the scrap metal industry and wants something nice, clean and very professional.

Industry/Entity Type

Business

Requirements
Must have
• Our logo
• Would probably be good to incorporate colors from logo into design.
• Example info we need on the cards.
• Name
• Company Address
• Cell Phone
• Office Phone
• Fax
• Email
• Company Website
Should not have
• Should not be too cluttered. Needs to be nice, clean and professional looking.

```html
<!DOCTYPE html>
<html lang="en">
<head>
<meta charset="utf-8">
<title>KTR Business Card</title>
<link rel="stylesheet" href="https://fonts.googleapis.com/css2?family=Roboto:wght@300;400&family=Open+Sans:wght@700&display=swap">
<style>
  :root {
    --page: #d9d9d9;
    --card-dark: #050505;
    --card-mid: #161616;
    --brand-blue: #1b8fd0;
    --brand-blue-deep: #1f4e8f;
    --text-white: #f2f2f2;
    --text-grey: #8c9198;
    --faint: rgba(255, 255, 255, 0.05);
  }
  * { box-sizing: border-box; margin: 0; padding: 0; }
  html, body {
    width: 1200px; height: 900px; overflow: hidden;
    background: radial-gradient(ellipse at 55% 40%, #eeeeee 0%, var(--page) 55%, #9a9a9a 100%);
    font-family: "Roboto", Arial, sans-serif;
  }
  .sheet {
    position: relative; width: 1200px; height: 900px;
  }
  .card {
    position: absolute; left: 250px; width: 700px; height: 400px;
    background: linear-gradient(135deg, var(--card-mid) 0%, var(--card-dark) 45%, #0d0d0d 100%);
    border-radius: 3px;
    box-shadow: 0 14px 30px rgba(0,0,0,0.35);
    overflow: hidden;
  }
  .card--front { top: 40px; }
  .card--back { top: 465px; }

  /* Front */
  .person { position: absolute; left: 36px; top: 82px; }
  .person__name {
    font-weight: 300; font-size: 48px; letter-spacing: 2px;
    color: var(--brand-blue); line-height: 1;
  }
  .person__title {
    margin-top: 8px; font-weight: 400; font-size: 17px;
    letter-spacing: 4.5px; color: var(--text-white);
  }
  .brand-small {
    position: absolute; right: 40px; top: 38px;
    display: flex; flex-direction: column; align-items: center; gap: 10px;
  }
  .brand-small__mark { width: 46px; height: 46px; background: var(--brand-blue); }
  .brand-small__name {
    font-family: "Open Sans", Arial, sans-serif; font-weight: 700;
    font-size: 15px; color: var(--text-grey);
  }
  .icon-tab {
    position: absolute; left: 0; top: 218px; width: 50px; height: 104px;
    background: var(--brand-blue); border-radius: 0 3px 3px 0;
    display: flex; flex-direction: column; justify-content: space-around; align-items: center;
    padding: 4px 0;
  }
  .icon-tab svg { width: 24px; height: 24px; }
  .contacts {
    position: absolute; left: 72px; top: 222px;
    list-style: none; color: var(--text-white); font-size: 16px;
  }
  .contacts li { height: 32px; line-height: 32px; }
  .watermark {
    position: absolute; right: 30px; bottom: 48px;
    font-family: "Open Sans", Arial, sans-serif; font-weight: 700;
    font-size: 30px; color: var(--faint);
  }

  /* Back */
  .brand-large {
    position: absolute; left: 0; right: 0; top: 88px;
    display: flex; flex-direction: column; align-items: center; gap: 26px;
  }
  .brand-large__mark { width: 110px; height: 110px; background: var(--brand-blue); }
  .brand-large__name {
    font-family: "Open Sans", Arial, sans-serif; font-weight: 700;
    font-size: 40px; color: var(--text-grey);
  }
  .edge-band {
    position: absolute; left: 0; right: 0; bottom: 0; height: 10px;
    background: linear-gradient(90deg, var(--brand-blue-deep), var(--brand-blue));
  }
</style>
</head>
<body>
<main class="sheet">
  <section class="card card--front" aria-label="Card front">
    <div class="person">
      <h1 class="person__name">DANIEL REED</h1>
      <p class="person__title">EXECUTIVE DIRECTOR</p>
    </div>
    <div class="brand-small">
      <div class="brand-small__mark"></div>
      <span class="brand-small__name">Keystone Trade Resources</span>
    </div>
    <div class="icon-tab">
      <svg viewBox="0 0 24 24" aria-hidden="true"><circle cx="12" cy="12" r="11" fill="none" stroke="#fff" stroke-width="1.4"/><path d="M8 6.5c-.8.6-1.3 1.6-.9 3 .9 3 3.5 5.8 6.4 7 1.4.5 2.4 0 3-.8l-2-1.9-1.5 1c-1.4-.6-2.8-2-3.4-3.4l1-1.5z" fill="#fff"/></svg>
      <svg viewBox="0 0 24 24" aria-hidden="true"><circle cx="12" cy="12" r="11" fill="none" stroke="#fff" stroke-width="1.4"/><rect x="6" y="8" width="12" height="8" fill="none" stroke="#fff" stroke-width="1.3"/><path d="M6 8l6 5 6-5" fill="none" stroke="#fff" stroke-width="1.3"/></svg>
      <svg viewBox="0 0 24 24" aria-hidden="true"><circle cx="12" cy="12" r="11" fill="none" stroke="#fff" stroke-width="1.4"/><circle cx="12" cy="12" r="6.5" fill="none" stroke="#fff" stroke-width="1.2"/><ellipse cx="12" cy="12" rx="3" ry="6.5" fill="none" stroke="#fff" stroke-width="1.1"/><path d="M5.5 12h13M6.5 9h11M6.5 15h11" stroke="#fff" stroke-width="1"/></svg>
    </div>
    <ul class="contacts">
      <li>+ 123 555 0147</li>
      <li>ktrbrokers@mail.com</li>
      <li>www.ktrbrokers.com</li>
    </ul>
    <span class="watermark">Keystone Trade Resources</span>
  </section>

  <section class="card card--back" aria-label="Card back">
    <div class="brand-large">
      <div class="brand-large__mark"></div>
      <span class="brand-large__name">Keystone Trade Resources</span>
    </div>
    <div class="edge-band"></div>
  </section>
</main>
</body>
</html>
```